Brightpath Letterhead

We would like a letterhead for our company. I have uploaded our logo.

Brightpath Ridge Consulting
1450 W Corliss Ave Ste 310
Cedar Hollow, TX 75218
833-517-2906

```html
<!DOCTYPE html>
<html lang="en">
<head>
<meta charset="utf-8">
<title>Brightpath Letterhead</title>
<link rel="stylesheet" href="https://fonts.googleapis.com/css2?family=Jost:wght@400;500;600&display=swap">
<style>
  :root {
    --backdrop: #c6c6c6;
    --paper: #ffffff;
    --ink-teal: #145566;
    --band-slate: #8aadb5;
    --band-mint: #b3e1cd;
    --mark-faint: #e3eeef;
  }
  * { box-sizing: border-box; margin: 0; padding: 0; }
  html, body {
    width: 1200px;
    height: 878px;
    overflow: hidden;
    background: var(--backdrop);
    font-family: "Jost", "Futura", sans-serif;
  }
  .canvas {
    position: relative;
    width: 1200px;
    height: 878px;
    display: flex;
    align-items: center;
    justify-content: center;
  }
  .letterhead {
    position: relative;
    width: 600px;
    height: 776px;
    background: var(--paper);
    box-shadow: 0 10px 30px rgba(0, 0, 0, 0.18);
    overflow: hidden;
  }
  .edge-bands {
    position: absolute;
    inset: 0;
    width: 100%;
    height: 100%;
  }
  .band-left { fill: var(--band-slate); }
  .band-right { fill: var(--band-mint); }
  .brand {
    position: absolute;
    top: 46px;
    left: 0;
    right: 0;
    display: flex;
    align-items: center;
    justify-content: center;
    gap: 12px;
  }
  .brand-dot {
    flex: none;
    width: 26px;
    height: 26px;
    border-radius: 50%;
    background: var(--ink-teal);
  }
  .brand-name {
    color: var(--ink-teal);
    font-weight: 600;
    font-size: 18px;
    letter-spacing: 0.14em;
    text-transform: uppercase;
    white-space: nowrap;
  }
  .watermark {
    position: absolute;
    left: 50%;
    top: 340px;
    width: 300px;
    height: 300px;
    margin-left: -150px;
    margin-top: -150px;
    border-radius: 50%;
    background: var(--mark-faint);
  }
  .contact {
    position: absolute;
    left: 40px;
    bottom: 30px;
    color: var(--ink-teal);
    font-size: 12px;
    font-weight: 400;
    line-height: 1.4;
    font-style: normal;
    letter-spacing: 0.02em;
    white-space: nowrap;
  }
</style>
</head>
<body>
  <main class="canvas">
    <article class="letterhead">
      <svg class="edge-bands" viewBox="0 0 600 776" preserveAspectRatio="none" aria-hidden="true">
        <path class="band-left" d="M0 0 H58 C40 260 22 520 0 776 Z"/>
        <path class="band-right" d="M600 0 V776 H534 C560 520 586 260 600 0 Z"/>
      </svg>

      <header class="brand">
        <span class="brand-dot"></span>
        <span class="brand-name">Brightpath Ridge Consulting</span>
      </header>

      <div class="watermark" aria-hidden="true"></div>

      <address class="contact">
        1450 W Corliss Ave Ste 310<br>
        Cedar Hollow, TX 75218<br>
        833-517-2906
      </address>
    </article>
  </main>
</body>
</html>
```